Re-Design Business Card and Logo for Plastic Printing

Business is a small financial planning (investments, insurance, retirement, etc.) firm. The majority of our clients are 55+ years old, professional occupations (pilots, doctors, bankers, etc.) but not necessarily "high net worth."
I would like to have a design that would be used on clear plastic business cards. I have found a vendor that makes these but I do not have the ability to design these like I want.
I do have one proof but I just don't feel like it's the right one for me. Also, I feel that I need some help with a logo redesign so maybe someone could handle that for me as well.
I want the final design to "eye catching" but still be tasteful. I am open to suggestion regarding colors and such.
I will include the old design as well as the new proof I have to give you an idea of what I current have. Keep in mind, I have no allegiance to the attached designs.
For the second file (Business Card New Proof), the white space shown will be transparent when printed on plastic card.
Target Market(s)
Mostly people age 55+ in professional occupations.
Industry/Entity Type
Financial Service
Contact Information for Business Card
Looking for design that can be printed on clear plastic cards (if possible).
Logo Text
HWC - Harborline Wealth Counsel
Requirements
Must have
- Must be double sided because disclosure is required for compliance reasons.
Designations (must include the Registered trademark symbol as follows)...
MBA, ChFC®, CLU®, CRPS®
Nice to have
- The little icons next to email, phone and fax are nice.
Should not have
- I think I would like to eliminate the Owner and Co-Founder line that you see on the attachments.

```html
<!DOCTYPE html>
<html lang="en">
<head>
<meta charset="utf-8">
<title>Harborline Wealth Counsel – Business Card</title>
<link rel="stylesheet" href="https://fonts.googleapis.com/css2?family=PT+Sans:ital,wght@0,400;0,700;1,400;1,700&display=swap">
<style>
  :root {
    --page-bg: #e3e3e3;
    --card-bg: #ededed;
    --card-edge: #d6d6d6;
    --navy: #1b3d6d;
    --sky: #7fa4cf;
    --ink-grey: #5d6166;
    --ghost-grey: #a3abb5;
    --white: #ffffff;
  }
  * { margin: 0; padding: 0; box-sizing: border-box; }
  html, body {
    width: 1200px; height: 960px; overflow: hidden;
    background: var(--page-bg);
    font-family: "PT Sans", Arial, sans-serif;
  }
  .canvas { position: relative; width: 1200px; height: 960px; }
  .card {
    position: absolute; left: 287px; width: 623px; height: 354px;
    border-radius: 22px; overflow: hidden;
    background: var(--card-bg);
    border: 1px solid var(--card-edge);
  }
  .card--back { top: 98px; }
  .card--front { top: 507px; }
  .card__shape { position: absolute; inset: 0; }

  .brand { display: flex; align-items: center; gap: 12px; width: 305px; flex: none; }
  .brand__dot { width: 16px; height: 16px; border-radius: 50%; background: currentColor; flex: none; }
  .brand__name {
    font-weight: 700; font-size: 29px; line-height: 29px;
    text-transform: uppercase; letter-spacing: 0.6px; white-space: nowrap;
  }
  .divider { width: 2px; height: 62px; background: currentColor; opacity: 0.6; flex: none; }
  .tagline { font-style: italic; font-size: 16px; line-height: 21px; white-space: nowrap; }

  /* back side: header seen through the clear card */
  .ghost-header {
    position: absolute; left: 70px; top: 40px; width: 510px; height: 64px;
    display: flex; align-items: center; gap: 26px;
    transform: scaleX(-1); color: var(--ghost-grey);
  }
  .disclosure {
    position: absolute; left: 36px; top: 232px; width: 440px;
    color: var(--white); font-size: 13.5px; line-height: 17.8px;
  }

  /* front side */
  .front-header {
    position: absolute; left: 45px; top: 40px; height: 64px;
    display: flex; align-items: center; gap: 26px; color: var(--ink-grey);
  }
  .front-header .brand { color: var(--navy); }
  .front-header .tagline { color: var(--ink-grey); font-weight: 700; }
  .front-header .divider { background: var(--ink-grey); opacity: 0.8; }

  .person { position: absolute; left: 42px; top: 252px; color: var(--white); }
  .person__name { font-weight: 700; font-size: 22px; line-height: 26px; }
  .person__titles { font-size: 15px; line-height: 20px; }
  .person__titles sup { font-size: 8px; }

  .contact {
    position: absolute; right: 34px; top: 187px; color: var(--white);
    font-size: 15.5px; line-height: 21px; text-align: right; list-style: none;
  }
  .contact__address { margin-bottom: 8px; }
  .contact__line { display: flex; justify-content: flex-end; align-items: center; gap: 6px; }
  .contact__line svg { width: 14px; height: 14px; flex: none; }
</style>
</head>
<body>
<main class="canvas">

  <section class="card card--back" aria-label="Card back">
    <svg class="card__shape" viewBox="0 0 623 354" aria-hidden="true">
      <defs>
        <linearGradient id="navyBack" x1="0" x2="1">
          <stop offset="0" stop-color="#264a78"/>
          <stop offset="0.45" stop-color="#1a3b6b"/>
          <stop offset="0.7" stop-color="#2b5080"/>
          <stop offset="1" stop-color="#1a3b6b"/>
        </linearGradient>
      </defs>
      <path d="M185,135 Q450,125 623,186 L623,248 Q450,150 185,135 Z" fill="var(--sky)"/>
      <path d="M0,177 Q300,100 623,252 L623,354 L0,354 Z" fill="url(#navyBack)"/>
    </svg>
    <div class="ghost-header">
      <div class="brand">
        <span class="brand__dot"></span>
        <span class="brand__name">Harborline<br>Wealth Counsel</span>
      </div>
      <span class="divider"></span>
      <p class="tagline">Steady Plans for<br>the Years Ahead</p>
    </div>
    <p class="disclosure">Marcus Ellery is a registered representative of and offers securities and advisory services through Beacon Ridge Securities Corporation, Member FSIA. Beacon Ridge Securities Corporation is a member of the Beacon Ridge Group which is the marketing name for Beacon Ridge National Corporation and its affiliates.</p>
  </section>

  <section class="card card--front" aria-label="Card front">
    <svg class="card__shape" viewBox="0 0 623 354" aria-hidden="true">
      <defs>
        <linearGradient id="navyFront" x1="0" x2="1">
          <stop offset="0" stop-color="#1a3b6b"/>
          <stop offset="0.55" stop-color="#1b3d6d"/>
          <stop offset="0.68" stop-color="#2c5182"/>
          <stop offset="1" stop-color="#1a3b6b"/>
        </linearGradient>
      </defs>
      <path d="M0,187 Q180,130 438,135 Q200,150 0,248 Z" fill="var(--sky)"/>
      <path d="M0,252 Q300,60 623,178 L623,354 L0,354 Z" fill="url(#navyFront)"/>
    </svg>
    <header class="front-header">
      <div class="brand">
        <span class="brand__dot"></span>
        <span class="brand__name">Harborline<br>Wealth Counsel</span>
      </div>
      <span class="divider"></span>
      <p class="tagline">Steady Plans for<br>the Years Ahead</p>
    </header>

    <div class="person">
      <h1 class="person__name">MARCUS ELLERY</h1>
      <p class="person__titles">MBA, ChFC<sup>®</sup>, CLU<sup>®</sup>, CRPS<sup>®</sup></p>
    </div>

    <ul class="contact">
      <li class="contact__address">2150 Cedarline Ave. Suite 310<br>Norfolk Bay, VA 23400</li>
      <li class="contact__line">(555) 014-2290
        <svg viewBox="0 0 24 24" aria-hidden="true"><path fill="#fff" d="M6.6 10.8a15.5 15.5 0 0 0 6.6 6.6l2.2-2.2c.3-.3.7-.4 1-.2 1.1.4 2.3.6 3.6.6.6 0 1 .4 1 1V20c0 .6-.4 1-1 1A17 17 0 0 1 3 4c0-.6.4-1 1-1h3.5c.6 0 1 .4 1 1 0 1.3.2 2.5.6 3.6.1.3 0 .7-.2 1z"/></svg></li>
      <li class="contact__line">Toll Free (555) 016-3381
        <svg viewBox="0 0 24 24" aria-hidden="true"><path fill="#fff" d="M6.6 10.8a15.5 15.5 0 0 0 6.6 6.6l2.2-2.2c.3-.3.7-.4 1-.2 1.1.4 2.3.6 3.6.6.6 0 1 .4 1 1V20c0 .6-.4 1-1 1A17 17 0 0 1 3 4c0-.6.4-1 1-1h3.5c.6 0 1 .4 1 1 0 1.3.2 2.5.6 3.6.1.3 0 .7-.2 1z"/></svg></li>
      <li class="contact__line">mellery@harborlinewc.com
        <svg viewBox="0 0 24 24" aria-hidden="true"><rect x="2.5" y="5.5" width="19" height="13" fill="none" stroke="#fff" stroke-width="2"/><path d="M2.5 5.5 12 13l9.5-7.5" fill="none" stroke="#fff" stroke-width="2"/></svg></li>
      <li class="contact__line">www.harborlinewc.com
        <svg viewBox="0 0 24 24" aria-hidden="true"><g fill="none" stroke="#fff" stroke-width="1.6"><circle cx="12" cy="12" r="9"/><ellipse cx="12" cy="12" rx="4" ry="9"/><path d="M3 12h18M4.5 7.5h15M4.5 16.5h15"/></g></svg></li>
    </ul>
  </section>

</main>
</body>
</html>
```